Merle's Brivolane Shower Banner

I need a banner design for a bridal shower. The banner size is 4 feet by 8 feet, so the artwork needs to be appropriately vertical (4'x8') I would like the design to be a fake brivolane post with the attached photo and hashtags.
Please add emoji's to the hashtags. hearts, and engagement ring, a tropical drink, a flip flop (if there is one.)

```html
<!DOCTYPE html>
<html lang="en">
<head>
<meta charset="utf-8">
<title>Merle's Brivolane Shower Banner</title>
<link rel="stylesheet" href="https://fonts.googleapis.com/css2?family=Open+Sans:wght@400;600;700&family=Yellowtail&family=Noto+Color+Emoji&display=block">
<style>
  :root {
    --paper: #ffffff;
    --ink: #222222;
    --muted: #8a8a8a;
    --rule: #d9d9d9;
    --tag-blue: #2f5fae;
    --button-blue: #3aa0e8;
    --heart-red: #e0262b;
    --nav-grey: #c8c8c8;
    --photo-top: #b23a3f;
    --photo-mid: #8c2a30;
    --photo-low: #6f1f25;
  }
  * { box-sizing: border-box; margin: 0; padding: 0; }
  html, body {
    width: 1200px; height: 2296px; overflow: hidden;
    background: var(--paper);
    font-family: "Open Sans", Arial, sans-serif;
    color: var(--ink);
  }
  .banner { position: relative; width: 1200px; height: 2296px; background: var(--paper); }

  .top-bar {
    position: absolute; left: 0; top: 0; width: 1200px; height: 158px;
    border-bottom: 4px solid var(--rule);
  }
  .top-bar .camera { position: absolute; left: 64px; top: 56px; width: 70px; height: 56px; }
  .top-bar .send { position: absolute; right: 64px; top: 52px; width: 64px; height: 60px; }
  .event-title {
    position: absolute; left: 0; right: 0; top: 20px; text-align: center;
    font-family: "Yellowtail", "Brush Script MT", "Segoe Script", cursive;
    font-weight: 400; font-size: 100px; line-height: 1; color: var(--ink);
  }
  .event-title span { display: inline-block; border-bottom: 5px solid var(--ink); padding: 0 8px 8px; }

  .post-header { position: absolute; left: 0; top: 190px; width: 1200px; height: 110px; }
  .avatar { position: absolute; left: 80px; top: 6px; width: 100px; height: 100px; }
  .account-name { position: absolute; left: 212px; top: 10px; font-weight: 700; font-size: 46px; line-height: 1.1; }
  .account-place { position: absolute; left: 212px; top: 66px; font-size: 30px; color: var(--muted); }
  .welcome-button {
    position: absolute; left: 790px; top: 20px; width: 256px; height: 72px;
    border: 4px solid var(--button-blue); border-radius: 8px;
    color: var(--button-blue); font-weight: 700; font-size: 42px;
    display: flex; align-items: center; justify-content: center;
  }
  .more-dots { position: absolute; left: 1096px; top: 22px; width: 20px; height: 70px; }

  .post-photo {
    position: absolute; left: 73px; top: 350px; width: 1054px; height: 1008px;
    background: linear-gradient(180deg, var(--photo-top) 0%, var(--photo-mid) 60%, var(--photo-low) 100%);
  }

  .action-row { position: absolute; left: 0; top: 1418px; width: 1200px; height: 76px; }
  .action-row svg { position: absolute; top: 0; height: 72px; }

  .likes { position: absolute; left: 86px; top: 1528px; font-size: 44px; display: flex; align-items: center; gap: 20px; }
  .likes svg { width: 30px; height: 28px; }

  .hashtags {
    position: absolute; left: 95px; top: 1630px; width: 1060px;
    font-size: 44px; line-height: 60px; color: var(--tag-blue); white-space: nowrap;
  }
  .emoji {
    font-family: "Noto Color Emoji", "Apple Color Emoji", "Segoe UI Emoji", sans-serif;
    font-size: 38px; margin-left: 8px;
  }

  .bottom-nav {
    position: absolute; left: 0; top: 2142px; width: 1200px; height: 154px;
    border-top: 4px solid var(--rule);
  }
  .bottom-nav svg { position: absolute; top: 56px; width: 62px; height: 62px; }
</style>
</head>
<body>
<main class="banner">

  <header class="top-bar">
    <svg class="camera" viewBox="0 0 70 56" aria-hidden="true">
      <path d="M6 12h16l6-9h14l6 9h16a4 4 0 0 1 4 4v34a4 4 0 0 1-4 4H6a4 4 0 0 1-4-4V16a4 4 0 0 1 4-4z" fill="var(--ink)"/>
      <circle cx="35" cy="32" r="13" fill="var(--paper)"/>
      <circle cx="35" cy="32" r="8" fill="var(--ink)"/>
    </svg>
    <h1 class="event-title"><span>Bridal Shower</span></h1>
    <svg class="send" viewBox="0 0 64 60" aria-hidden="true">
      <path d="M2 26 62 2 44 58 30 34z" fill="var(--ink)"/>
      <path d="M30 34 62 2" stroke="var(--paper)" stroke-width="4"/>
    </svg>
  </header>

  <section class="post-header">
    <svg class="avatar" viewBox="0 0 100 100" aria-hidden="true">
      <circle cx="50" cy="50" r="50" fill="var(--ink)"/>
      <circle cx="50" cy="40" r="15" fill="var(--paper)"/>
      <path d="M24 76c4-14 14-20 26-20s22 6 26 20z" fill="var(--paper)"/>
    </svg>
    <p class="account-name">Merle</p>
    <p class="account-place">Nullam, Dictum</p>
    <div class="welcome-button">Welcome</div>
    <svg class="more-dots" viewBox="0 0 20 70" aria-hidden="true">
      <circle cx="10" cy="12" r="6" fill="var(--ink)"/>
      <circle cx="10" cy="35" r="6" fill="var(--ink)"/>
      <circle cx="10" cy="58" r="6" fill="var(--ink)"/>
    </svg>
  </section>

  <div class="post-photo" role="img" aria-label="Photo of the engaged couple smiling in red football jerseys inside a stadium"></div>

  <section class="action-row">
    <svg style="left:88px;width:76px" viewBox="0 0 76 72" aria-label="Liked">
      <path d="M38 68 8 38C-2 26 4 6 20 6c8 0 14 5 18 11C42 11 48 6 56 6c16 0 22 20 12 32z" fill="var(--heart-red)"/>
    </svg>
    <svg style="left:200px;width:72px" viewBox="0 0 72 72" aria-hidden="true">
      <path d="M36 6a30 30 0 1 0 22 50l10 8-3-14A30 30 0 0 0 36 6z" fill="none" stroke="var(--ink)" stroke-width="5" stroke-linejoin="round"/>
    </svg>
    <svg style="left:306px;width:72px" viewBox="0 0 72 72" aria-hidden="true">
      <path d="M4 10h64L32 66 28 36z M28 36 68 10" fill="none" stroke="var(--ink)" stroke-width="5" stroke-linejoin="round"/>
    </svg>
    <svg style="left:1064px;width:56px" viewBox="0 0 56 72" aria-hidden="true">
      <path d="M5 4h46v64L28 48 5 68z" fill="none" stroke="var(--ink)" stroke-width="5" stroke-linejoin="round"/>
    </svg>
  </section>

  <p class="likes">
    <svg viewBox="0 0 30 28" aria-hidden="true"><path d="M15 27 3 15C-1 10 1 2 8 2c3 0 5 2 7 4 2-2 4-4 7-4 7 0 9 8 5 13z" fill="var(--ink)"/></svg>
    1204 likes
  </p>

  <p class="hashtags">
    #merle'sshower #summerwedding<span class="emoji">💕</span><br>
    #happilyeverafter #futbolfun<span class="emoji">💍</span><br>
    #merleandtobin2018 #tobinscored!<span class="emoji">❤️</span><br>
    #marriagegoals #trueloveforever<span class="emoji">💖</span><br>
    #harborvalebliss<span class="emoji">🍹</span><span class="emoji">🩴</span><br>
    #goeagles! #harborvalecollege'13<span class="emoji">💕</span><br>
    #sportycouple#playtogetherstaytogether<span class="emoji">💍</span>
  </p>

  <nav class="bottom-nav">
    <svg style="left:96px" viewBox="0 0 62 62" aria-label="Home">
      <path d="M4 30 31 6l27 24h-7v26H38V40H24v16H11V30z" fill="var(--ink)"/>
    </svg>
    <svg style="left:342px" viewBox="0 0 62 62" aria-label="Search">
      <circle cx="26" cy="26" r="17" fill="none" stroke="var(--nav-grey)" stroke-width="6"/>
      <path d="M39 39 56 56" stroke="var(--nav-grey)" stroke-width="7" stroke-linecap="round"/>
    </svg>
    <svg style="left:569px" viewBox="0 0 62 62" aria-label="New post">
      <rect x="4" y="4" width="54" height="54" rx="8" fill="var(--nav-grey)"/>
      <path d="M31 16v30M16 31h30" stroke="var(--paper)" stroke-width="6"/>
    </svg>
    <svg style="left:795px" viewBox="0 0 62 62" aria-label="Activity">
      <path d="M31 58 7 34C-1 25 3 6 18 6c6 0 10 3 13 8 3-5 7-8 13-8 15 0 19 19 11 28z" fill="var(--nav-grey)"/>
    </svg>
    <svg style="left:1042px" viewBox="0 0 62 62" aria-label="Profile">
      <circle cx="31" cy="20" r="14" fill="var(--nav-grey)"/>
      <path d="M4 58c2-16 13-22 27-22s25 6 27 22z" fill="var(--nav-grey)"/>
    </svg>
  </nav>

</main>
</body>
</html>
```